Manufacturing company needs new business card.

I need a unique Business Card that will truly stand out. Nothing too busy. Simple is good, right? Not looking for a standard design either. No cookie cutter layout. I am just looking for something interesting and a bit different. Does't have to completely off the wall crazy, just not your run of the mill business card. Clean and modern with a touch of industrial.

Target Market(s)

Air conditioning industry, Architects, builders.

Industry/Entity Type

Business

Contact Information for Business Card

Details to be included on card are:

Peter Vance
Managing Director

T: 1300 847 519
M: 0428 593 174
W: www.brenvaleworks.com.au
E: peter.vance@brenvaleworks.com.au
A: 58 Harwick Lane, Sydney NSW 2000

Font styles to use
Sans Serif

Colors
0355a3
848484
fbfbfb

Requirements
Must have
• Card design must be landscape.

```html
<!DOCTYPE html>
<html lang="en">
<head>
<meta charset="utf-8">
<title>Brenvale Works – Business Card</title>
<link rel="stylesheet" href="https://fonts.googleapis.com/css2?family=Karla:wght@400;500;700&display=swap">
<style>
  :root {
    --brand-blue: #3256a4;
    --steel-grey: #848484;
    --ink: #2b2b2b;
    --card-white: #ffffff;
    --backdrop: #ece9e4;
  }
  * { box-sizing: border-box; margin: 0; padding: 0; }
  html, body {
    width: 1200px;
    height: 1200px;
    overflow: hidden;
    background: var(--backdrop);
    font-family: "Karla", Arial, sans-serif;
  }
  .canvas {
    position: relative;
    width: 1200px;
    height: 1200px;
  }
  .card {
    position: absolute;
    width: 780px;
    height: 478px;
    background: var(--card-white);
    box-shadow: 0 10px 30px rgba(0, 0, 0, 0.12);
    overflow: hidden;
  }

  /* Front */
  .card--front { left: 80px; top: 90px; }
  .accent-bar {
    position: absolute;
    width: 38px;
    background: var(--brand-blue);
  }
  .accent-bar--left { left: 0; top: 250px; height: 160px; }
  .accent-bar--right { right: 0; top: 70px; height: 160px; }
  .brand-lockup {
    position: absolute;
    left: 50%;
    top: 50%;
    transform: translate(-50%, -50%);
    display: flex;
    align-items: center;
    gap: 22px;
  }
  .brand-mark {
    width: 56px;
    height: 56px;
    background: var(--brand-blue);
  }
  .brand-name {
    font-size: 52px;
    font-weight: 500;
    color: var(--brand-blue);
    letter-spacing: -0.5px;
    white-space: nowrap;
  }

  /* Back */
  .card--back { left: 340px; top: 632px; }
  .contact-label { color: var(--brand-blue); font-weight: 700; }
  .contact-line {
    font-size: 23px;
    color: var(--ink);
    line-height: 1.3;
  }
  .phone-row {
    position: absolute;
    top: 70px;
    left: 0;
    width: 100%;
    text-align: center;
  }
  .person {
    position: absolute;
    left: 0;
    top: 198px;
    width: 390px;
    text-align: center;
  }
  .person-name {
    font-size: 36px;
    font-weight: 700;
    color: var(--brand-blue);
    letter-spacing: 0.5px;
  }
  .person-role {
    font-size: 23px;
    color: var(--ink);
    margin-top: 6px;
  }
  .address-panel {
    position: absolute;
    left: 390px;
    right: 0;
    top: 160px;
    height: 160px;
    background: var(--brand-blue);
    display: flex;
    align-items: center;
    justify-content: center;
    text-align: center;
  }
  .address-panel .contact-line,
  .address-panel .contact-label { color: var(--card-white); }
  .online-rows {
    position: absolute;
    left: 0;
    top: 356px;
    width: 100%;
    text-align: center;
  }
</style>
</head>
<body>
<main class="canvas">

  <section class="card card--front" aria-label="Business card front">
    <div class="accent-bar accent-bar--left"></div>
    <div class="accent-bar accent-bar--right"></div>
    <div class="brand-lockup">
      <div class="brand-mark"></div>
      <span class="brand-name">Brenvale Works</span>
    </div>
  </section>

  <section class="card card--back" aria-label="Business card back">
    <p class="phone-row contact-line">
      <span class="contact-label">T:</span> 1300 847 519, <span class="contact-label">M:</span> 0428 593 174
    </p>

    <div class="person">
      <h1 class="person-name">Peter Vance</h1>
      <p class="person-role">Managing Director</p>
    </div>

    <div class="address-panel">
      <p class="contact-line">
        <span class="contact-label">A:</span> 58 Harwick Lane<br>
        Sydney NSW 2000
      </p>
    </div>

    <div class="online-rows">
      <p class="contact-line"><span class="contact-label">W:</span> www.brenvaleworks.com.au</p>
      <p class="contact-line"><span class="contact-label">E:</span> peter.vance@brenvaleworks.com.au</p>
    </div>
  </section>

</main>
</body>
</html>
```